Brightwell Harbor Property Maintenance and Construction Company require new business card design

We are a property maintenance and construction company that offer a total range of property maintenance construction services and have been too busy dealing with the running of the office and completing jobs to update our business cards. We have recently had a new logo designed for us and are needing to update our cards (and we also have new staff requiring business cards. We would ideally want to stay with the orange, black and grey theme. I have attached current business cards and also our new logo. Looking forward to feedback and ideas.

Target Market(s)

Real estate agents, local governments, companies, residential

Industry/Entity Type

Property Maintenance

Contact Information for Business Card

File uploaded has names and phone numbers for staff. We also need to add a card for a new staff member, which can be provided.

Colors
f37022

Requirements
Must have
• Must have logos for Certified Fabrication Steward and Prime Erector for which we are members of. Also a description of what services we provide
Should not have
• any "flowery" fonts and design. We are a construction company, so probably something very standard...but also not just a regular font (ie Arial!)

```html
<!DOCTYPE html>
<html lang="en">
<head>
<meta charset="utf-8">
<title>Brightwell Harbor Business Card</title>
<link rel="stylesheet" href="https://fonts.googleapis.com/css2?family=Open+Sans:ital,wght@0,400;0,600;0,700;1,400&display=swap">
<style>
  :root {
    --orange: #f37022;
    --orange-deep: #e2601a;
    --charcoal: #2b2b2b;
    --grey: #6d6e70;
    --grey-light: #a7a9ac;
    --paper: #ffffff;
    --backdrop: #ececec;
  }
  * { box-sizing: border-box; margin: 0; padding: 0; }
  html, body { width: 1200px; height: 900px; overflow: hidden; }
  body {
    background: var(--backdrop);
    font-family: "Open Sans", sans-serif;
    position: relative;
  }
  .card {
    position: absolute;
    width: 560px;
    height: 320px;
    border-radius: 3px;
    overflow: hidden;
    box-shadow: 0 8px 22px rgba(0,0,0,0.18);
  }

  /* Back of card: services and memberships */
  .card-back {
    left: 60px; top: 120px;
    background: linear-gradient(160deg, var(--orange) 0%, var(--orange-deep) 100%);
    color: var(--paper);
    padding: 34px 40px;
  }
  .services-title {
    font-weight: 700;
    font-size: 22px;
    margin-bottom: 16px;
  }
  .back-columns { display: flex; justify-content: space-between; align-items: center; }
  .services-list { list-style: none; }
  .services-list li {
    position: relative;
    padding-left: 18px;
    font-weight: 600;
    font-size: 18px;
    line-height: 28px;
  }
  .services-list li::before {
    content: "";
    position: absolute;
    left: 0; top: 11px;
    width: 7px; height: 7px;
    border-radius: 50%;
    background: var(--paper);
  }
  .memberships {
    display: flex;
    flex-direction: column;
    gap: 18px;
    margin-right: 10px;
  }
  .membership-badge {
    width: 100px; height: 90px;
    border-radius: 6px;
    background: var(--paper);
    box-shadow: 0 2px 6px rgba(0,0,0,0.15);
  }

  /* Front of card: contact details */
  .card-front {
    left: 580px; top: 460px;
    background: var(--paper);
  }
  .brand {
    position: absolute;
    top: 48px; left: 0; right: 0;
    display: flex;
    justify-content: center;
    align-items: center;
    gap: 12px;
    padding-left: 70px;
  }
  .brand-mark {
    width: 22px; height: 22px;
    background: var(--orange);
  }
  .brand-name {
    font-weight: 700;
    font-size: 32px;
    color: var(--charcoal);
  }
  .person {
    position: absolute;
    top: 140px; right: 300px;
    text-align: right;
    color: var(--grey);
  }
  .person-name {
    font-weight: 700;
    font-size: 24px;
    color: var(--orange);
    line-height: 30px;
  }
  .person-role { font-size: 15px; line-height: 20px; margin-bottom: 10px; }
  .person-address { font-size: 15px; line-height: 21px; font-style: italic; }
  .divider {
    position: absolute;
    top: 146px; left: 276px;
    width: 1px; height: 112px;
    background: var(--grey-light);
  }
  .contact-list {
    position: absolute;
    top: 146px; left: 292px;
    list-style: none;
    color: var(--grey);
    font-size: 15px;
    line-height: 22px;
  }
  .contact-list li { display: flex; align-items: center; gap: 9px; }
  .contact-list svg { width: 12px; height: 12px; fill: var(--orange); flex: none; }
  .front-wave {
    position: absolute;
    left: 0; bottom: 0;
    width: 560px; height: 80px;
  }
</style>
</head>
<body>

<section class="card card-back">
  <h2 class="services-title">Offering All Property Maintenance Services</h2>
  <div class="back-columns">
    <ul class="services-list">
      <li>Programmed Maintenance</li>
      <li>Essential Services</li>
      <li>Maintenance Planning</li>
      <li>Reactionary Maintenance</li>
      <li>Commercial / Residential</li>
      <li>Body Corporate</li>
      <li>Insurance Claims</li>
      <li>24 Hour On Call</li>
    </ul>
    <div class="memberships">
      <span class="membership-badge" role="img" aria-label="Certified Fabrication Steward membership badge"></span>
      <span class="membership-badge" role="img" aria-label="Prime Erector membership badge"></span>
    </div>
  </div>
</section>

<section class="card card-front">
  <div class="brand">
    <span class="brand-mark"></span>
    <span class="brand-name">Brightwell Harbor</span>
  </div>

  <div class="person">
    <p class="person-name">Daniel Okafor</p>
    <p class="person-role">Managing Member</p>
    <p class="person-address">2217 Alder Creek Road,<br>Riverton, CA 95760</p>
  </div>

  <span class="divider"></span>

  <ul class="contact-list">
    <li><svg viewBox="0 0 12 12"><path d="M2.5 0.5l2 2.3-1.2 1.4c.8 1.7 2 2.9 3.6 3.7l1.4-1.2 2.2 2-1.2 2.3C4.6 10.6 1.3 7.3.5 2.1z"/></svg>(555) 214-3080</li>
    <li><svg viewBox="0 0 12 12"><rect x="3" y="0.5" width="6" height="3.5"/><rect x="0.5" y="4.5" width="11" height="5" rx="1"/><rect x="3" y="8" width="6" height="3.5"/></svg>(555) 214-3081</li>
    <li><svg viewBox="0 0 12 12"><path d="M3 0h6a1 1 0 0 1 1 1v10a1 1 0 0 1-1 1H3a1 1 0 0 1-1-1V1a1 1 0 0 1 1-1zm.5 1.5v7.5h5V1.5z"/></svg>(555) 709-4412</li>
    <li><svg viewBox="0 0 12 12"><path d="M0 2h12v1L6 7 0 3zM0 4.4l6 4 6-4V10H0z"/></svg>daniel@bwharbor.example</li>
    <li><svg viewBox="0 0 12 12"><circle cx="6" cy="6" r="5.5"/><path d="M.5 6h11M6 .5c-2.5 3-2.5 8 0 11M6 .5c2.5 3 2.5 8 0 11" stroke="#fff" stroke-width=".8" fill="none"/></svg>www.bwharbor.example</li>
  </ul>

  <svg class="front-wave" viewBox="0 0 560 80" preserveAspectRatio="none" aria-hidden="true">
    <path d="M0 28 C140 4 300 20 400 38 C470 50 520 40 560 24 L560 34 C520 52 470 60 400 50 C300 34 150 20 0 40 Z" fill="var(--grey)"/>
    <path d="M0 42 C150 24 300 36 400 54 C470 66 520 56 560 38 L560 80 L0 80 Z" fill="var(--orange)"/>
  </svg>
</section>

</body>
</html>
```